Stationary for a property rental company
Glenbrook Rentals
Stationary for a property rental company - Real Estate
Creative Brief
Simple
Marla Pike
Owner
PO Box 7413 Ashford Falls, VT 05199
marla@glenbrookrentals-example.net
www.glenbrookrentals-example.net
Please use similar colors that are found in the Logo.
Use emblem for the back of the card

```html
<!DOCTYPE html>
<html lang="en">
<head>
<meta charset="utf-8">
<title>Glenbrook Rentals – Business Card</title>
<link href="https://fonts.googleapis.com/css2?family=Cinzel:wght@400;600&family=Lato:wght@400&display=swap" rel="stylesheet">
<style>
  :root {
    --canvas: #e9eaec;
    --brand-blue: #5e95c0;
    --deep-blue: #3f74a0;
    --leaf-green: #8fb03a;
    --paper: #ffffff;
    --ink-soft: #6c8fab;
  }
  * { box-sizing: border-box; margin: 0; padding: 0; }
  html, body { width: 1200px; height: 864px; overflow: hidden; }
  body {
    background: var(--canvas);
    font-family: "Lato", sans-serif;
    position: relative;
  }
  .card {
    position: absolute;
    left: 280px;
    width: 640px;
    height: 366px;
    border-radius: 20px;
    overflow: hidden;
    box-shadow: 0 6px 18px rgba(0,0,0,.18);
  }
  /* back */
  .card-back { top: 40px; background: var(--brand-blue); }
  .back-mark {
    position: absolute; left: 0; right: 0; top: 130px;
    display: flex; align-items: center; justify-content: center; gap: 14px;
  }
  .mark-dot { width: 30px; height: 30px; border-radius: 50%; background: var(--paper); flex: none; }
  .mark-name {
    font-family: "Cinzel", serif; font-weight: 600; font-size: 30px;
    letter-spacing: 3px; color: var(--paper); white-space: nowrap;
  }
  .back-web {
    position: absolute; left: 0; right: 0; top: 232px; text-align: center;
    font-family: "Cinzel", serif; font-size: 14px; letter-spacing: 3px; color: var(--paper);
  }
  /* front */
  .card-front { top: 458px; background: var(--paper); }
  .card-front svg.shape { position: absolute; inset: 0; }
  .front-mark {
    position: absolute; left: 40px; top: 165px;
    display: flex; align-items: center; gap: 9px;
  }
  .front-mark .mark-dot { width: 20px; height: 20px; background: var(--brand-blue); }
  .front-mark .mark-name { font-size: 19px; color: var(--deep-blue); letter-spacing: 2px; }
  .person { position: absolute; left: 42px; top: 232px; }
  .person-name {
    font-family: "Cinzel", serif; font-size: 15px; letter-spacing: 2px; color: var(--ink-soft);
  }
  .person-role {
    font-family: "Cinzel", serif; font-size: 11px; letter-spacing: 2px; color: var(--ink-soft); margin-top: 4px;
  }
  .contacts {
    position: absolute; right: 26px; top: 92px; list-style: none;
    display: flex; flex-direction: column; gap: 11px;
  }
  .contacts li {
    display: flex; align-items: center; gap: 8px;
    font-size: 10.5px; color: var(--paper); letter-spacing: .3px; white-space: nowrap;
  }
  .contacts svg { width: 15px; height: 15px; flex: none; }
</style>
</head>
<body>

<section class="card card-back" aria-label="Card back">
  <div class="back-mark">
    <span class="mark-dot"></span>
    <span class="mark-name">Glenbrook Rentals</span>
  </div>
  <p class="back-web">www.glenbrookrentals-example.net</p>
</section>

<section class="card card-front" aria-label="Card front">
  <svg class="shape" viewBox="0 0 640 366" preserveAspectRatio="none" aria-hidden="true">
    <path d="M200 0 C 300 50 360 150 390 366 L 640 366 L 640 0 Z" fill="#5e95c0"/>
    <path d="M184 0 C 284 54 342 152 370 366" fill="none" stroke="#8fb03a" stroke-width="7"/>
  </svg>

  <div class="front-mark">
    <span class="mark-dot"></span>
    <span class="mark-name">Glenbrook Rentals</span>
  </div>
  <div class="person">
    <p class="person-name">Marla Pike</p>
    <p class="person-role">Owner</p>
  </div>

  <ul class="contacts">
    <li>
      <svg viewBox="0 0 16 16"><path d="M8 1.5a4.5 4.5 0 0 0-4.5 4.5c0 3.4 4.5 8.5 4.5 8.5s4.5-5.1 4.5-8.5A4.5 4.5 0 0 0 8 1.5zm0 6.3a1.8 1.8 0 1 1 0-3.6 1.8 1.8 0 0 1 0 3.6z" fill="#fff"/></svg>
      <span>PO Box 7413<br>Ashford Falls, VT 05199</span>
    </li>
    <li>
      <svg viewBox="0 0 16 16"><path d="M4.2 1.8l2 2.6-1.2 1.5c.9 2 2.4 3.5 4.4 4.4l1.5-1.2 2.6 2-1 2.3C7 13.2 2.8 9 2 3z" fill="#fff"/></svg>
      <span>(802) 555-0147</span>
    </li>
    <li>
      <svg viewBox="0 0 16 16"><rect x="1.5" y="3.5" width="13" height="9" rx="1" fill="none" stroke="#fff" stroke-width="1.4"/><path d="M2 4l6 5 6-5" fill="none" stroke="#fff" stroke-width="1.4"/></svg>
      <span>marla@glenbrookrentals-example.net</span>
    </li>
    <li>
      <svg viewBox="0 0 16 16"><circle cx="8" cy="8" r="6.3" fill="none" stroke="#fff" stroke-width="1.3"/><path d="M1.7 8h12.6M8 1.7c-3 3.4-3 9.2 0 12.6M8 1.7c3 3.4 3 9.2 0 12.6" fill="none" stroke="#fff" stroke-width="1.1"/></svg>
      <span>www.glenbrookrentals-example.net</span>
    </li>
  </ul>
</section>

</body>
</html>
```